Etiketten-Design für Wein
Zielgruppe
Wir produzieren Wein und sind auf der Suche nach einer innovativen Weinetikette, welche sich durch unsere Weinvariationen durchziehen lässt.
Für das stehen wir ein: Nachhaltigkeit, moderne Landwirtschaft, Familienbetrieb, zukunftsorientiert, im Einklang mi der Natur, Freude an Pflanzen und Tieren.
Was uns gefällt: Relief / Prägung, eher schlichte, moderne und edle Etiketten, allenfalls Elemente aus der Natur, die auf Nachhaltigkeit hinweisen
Das möchten wir nicht auf der Etikette: zu knallige Farben, Comicfiguren oder ähnliches.
Unsere Weine werden direkt vermarktet und sollen aufgrund ihrer Etikette aus dem Weinregal herausstechen und ein Eyecatcher für die Kund:innen sein. Auch in einem Restaurant sollen sie als edlen Wein präsentiert werden können. Wir möchten, dass die Weinetiketten ein Storytelling mit sich bringen in Bezug auf die obenstehenden Punkte, für die wir einstehen.
Unsere Zielgruppe: Qualitätsbewusste Weingeniesser, mittleren und jüngeren Alters
Aufgabenstellung
Folgende Angaben sind auf der Etikette erforderlich:
- Weinsorte: Reserva / Riesling / Blauburgunder / Federweisser
- Name: Sennbachgut (kann klein und schlicht, unauffällig sein)
Unser Logo kann in Etikette aufgegriffen werden (auch in angepasster Form), ist aber nicht zwingend nötig. Das Logo ist auch eher revisionsbedürftig. ????
Folgende Masse sollte die Etikette ca. haben:
- Breite 95 mm
- Höhe 80 mm

```html
<!DOCTYPE html>
<html lang="de">
<head>
<meta charset="utf-8">
<title>Sennbachgut – Reserva Etikette</title>
<link href="https://fonts.googleapis.com/css2?family=Abril+Fatface&family=Josefin+Sans:wght@300;400&display=swap" rel="stylesheet">
<style>
  :root {
    --backdrop: #e9eaec;
    --paper: #fbfbf9;
    --gold: #c2a26a;
    --gold-line: #cdb487;
    --ink: #2b2b2b;
    --leaf-tint: #f1ebdf;
  }
  html, body {
    margin: 0;
    width: 1200px;
    height: 900px;
    overflow: hidden;
    background: var(--backdrop);
  }
  .canvas {
    position: relative;
    width: 1200px;
    height: 900px;
    display: flex;
    align-items: center;
    justify-content: center;
  }
  .label {
    position: relative;
    width: 760px;
    height: 640px;
    background: var(--paper);
    box-shadow: 0 2px 10px rgba(0,0,0,0.06);
  }
  .label__frame {
    position: absolute;
    left: 200px;
    top: 120px;
    width: 360px;
    height: 400px;
    border: 1.5px solid var(--gold-line);
    box-sizing: border-box;
  }
  .label__divider {
    position: absolute;
    left: 200px;
    top: 300px;
    width: 360px;
    height: 0;
    border-top: 1.5px solid var(--gold-line);
  }
  .label__estate {
    position: absolute;
    left: 236px;
    top: 152px;
    margin: 0;
    font-family: "Josefin Sans", sans-serif;
    font-weight: 400;
    font-size: 17px;
    letter-spacing: 0.28em;
    color: var(--ink);
  }
  .label__variety {
    position: absolute;
    left: 232px;
    top: 196px;
    margin: 0;
    font-family: "Abril Fatface", serif;
    font-weight: 400;
    font-size: 74px;
    line-height: 1;
    color: var(--gold);
  }
  .label__volume {
    position: absolute;
    left: 236px;
    top: 330px;
    margin: 0;
    font-family: "Josefin Sans", sans-serif;
    font-weight: 400;
    font-size: 17px;
    letter-spacing: 0.14em;
    color: var(--ink);
  }
  .label__leaf {
    position: absolute;
    left: 470px;
    top: 400px;
    width: 150px;
    height: 190px;
  }
</style>
</head>
<body>
  <main class="canvas">
    <section class="label">
      <div class="label__frame"></div>
      <div class="label__divider"></div>
      <p class="label__estate">SENNBACHGUT</p>
      <h1 class="label__variety">Reserva.</h1>
      <p class="label__volume">14 % VOL</p>
      <svg class="label__leaf" role="img" aria-label="Feine Linienzeichnung eines Blattzweigs in Goldbeige" viewBox="0 0 150 190">
        <rect x="0" y="0" width="150" height="190" rx="60" fill="var(--leaf-tint)" opacity="0.7"/>
      </svg>
    </section>
  </main>
</body>
</html>
```